Welcome Postcard for existing church in new facility

I need a postcard to express the 4 strong points of our ministry. I have attached a sample postcard that we really liked as a start point. Our four strengths are;

LOVE
WORSHIP
DIVERSITY
DOCTRINE

I want to make sure the colors used are vivid and provide plenty of pop.

I have provide images to coincide with the four ministry strengths and they are named according the the strength the coincide with, pick whichever you think is best graphically.

our twitter handle is @BRAVOHOPETX
our FB handle is /BRAVOHOPETX
our Youtube handle is /GraceHarbored

I must have all PSD layers in case last minutes changes need to be made. THIS IS A REQUIREMENT.
Updates

Project Deadline Extended
Reason: Not enough options being proposed yet

Target Market(s)

General Population

Industry/Entity Type

Non-Profit

Font styles to use
Sans Serif

Requirements
Must have
• I must have all PSD layers in case last minutes changes need to be made. THIS IS A REQUIREMENT.
Nice to have
• Be attractive and market friendly is US marketplace
Should not have
• Please do not submit multiple designs with slight deviations. If you submit multiple designs please make them totally different one from another. We will not consider your design if you spam us.

```html
<!DOCTYPE html>
<html lang="en">
<head>
<meta charset="utf-8">
<title>Grace Harbor Ministries – Welcome Postcard</title>
<link href="https://fonts.googleapis.com/css2?family=Montserrat:wght@300;400;500;600;700&display=swap" rel="stylesheet">
<style>
  :root {
    --backdrop: #dcdcd8;
    --ink: #000000;
    --paper: #ffffff;
    --love: #e8428f;
    --love-deep: #b13c8e;
    --worship: #f5952b;
    --worship-deep: #ef6a22;
    --diversity: #2fb14b;
    --diversity-deep: #5f7a2c;
    --doctrine: #1b7cc4;
    --doctrine-deep: #2a3f55;
    --link: #3a8fd0;
    --rule: #5a5a5a;
  }
  html, body {
    margin: 0;
    width: 1200px;
    height: 900px;
    overflow: hidden;
    background: var(--backdrop);
  }
  .postcard {
    position: absolute;
    left: 298px;
    top: 20px;
    width: 604px;
    height: 860px;
    box-shadow: 0 6px 24px rgba(0,0,0,.25);
  }
  .postcard svg { display: block; width: 100%; height: 100%; }
  .brand-name, .address, .tagline, .handle, .website, .monogram, .strength {
    font-family: "Montserrat", sans-serif;
    fill: var(--paper);
  }
  .monogram { font-weight: 700; font-size: 50px; }
  .brand-name { font-weight: 300; font-size: 38px; }
  .address { font-weight: 300; font-size: 23px; }
  .strength { font-weight: 500; font-size: 70px; }
  .tagline { font-weight: 400; font-size: 17px; }
  .handle { font-weight: 700; font-size: 11px; }
  .social-square { fill: var(--link); }
  .website { font-weight: 400; font-size: 19px; letter-spacing: 6px; fill: var(--link); }
</style>
</head>
<body>
<main class="postcard">
  <svg viewBox="0 0 710 1012" xmlns="http://www.w3.org/2000/svg">
    <defs>
      <linearGradient id="love-fill" x1="0" x2="1">
        <stop offset="0" stop-color="var(--love)"/>
        <stop offset="0.55" stop-color="#c95a9e"/>
        <stop offset="1" stop-color="var(--love-deep)"/>
      </linearGradient>
      <linearGradient id="worship-fill" x1="0" x2="1">
        <stop offset="0" stop-color="#3a2c22"/>
        <stop offset="0.45" stop-color="#7a5a35"/>
        <stop offset="0.8" stop-color="var(--worship)"/>
        <stop offset="1" stop-color="var(--worship-deep)"/>
      </linearGradient>
      <linearGradient id="diversity-fill" x1="0" x2="1">
        <stop offset="0" stop-color="var(--diversity)"/>
        <stop offset="0.5" stop-color="#4e8a36"/>
        <stop offset="1" stop-color="var(--diversity-deep)"/>
      </linearGradient>
      <linearGradient id="doctrine-fill" x1="0" x2="1">
        <stop offset="0" stop-color="var(--doctrine-deep)"/>
        <stop offset="0.5" stop-color="#3a6c95"/>
        <stop offset="1" stop-color="var(--doctrine)"/>
      </linearGradient>
    </defs>

    <rect class="card-base" width="710" height="1012" fill="var(--ink)"/>

    <g class="masthead">
      <text class="monogram" x="60" y="92">GH</text>
      <text class="brand-name" x="160" y="80">Grace Harbor Ministries</text>
      <line x1="115" y1="110" x2="595" y2="110" stroke="var(--rule)" stroke-width="1.5"/>
      <text class="address" x="355" y="141" text-anchor="middle">2480 West Laurel Ave, Mesquite, TX 75150</text>
    </g>

    <g class="band band-love">
      <polygon role="img" aria-label="Photo: two women embracing warmly, tinted pink" points="0,202 710,162 710,387 0,342" fill="url(#love-fill)"/>
      <text class="strength" x="45" y="297" textLength="180" lengthAdjust="spacingAndGlyphs">LOVE</text>
      <text class="tagline" x="247" y="267">Not simply a feeling, but</text>
      <text class="tagline" x="247" y="288">a decision and a commitment.</text>
    </g>

    <g class="band band-worship">
      <polygon role="img" aria-label="Photo: musician at keyboard and singer leading a congregation, tinted orange" points="0,348 710,393 710,542 0,588" fill="url(#worship-fill)"/>
      <text class="tagline" x="300" y="468" text-anchor="end">The natural reaction to the</text>
      <text class="tagline" x="300" y="489" text-anchor="end">very presence of the Lord.</text>
      <text class="strength" x="330" y="497" textLength="325" lengthAdjust="spacingAndGlyphs">WORSHIP</text>
    </g>

    <g class="band band-diversity">
      <polygon role="img" aria-label="Photo: congregation members praying with raised hands, tinted green" points="0,598 710,548 710,777 0,732" fill="url(#diversity-fill)"/>
      <text class="strength" x="45" y="692" textLength="355" lengthAdjust="spacingAndGlyphs">DIVERSITY</text>
      <text class="tagline" x="413" y="663">Unique individuals,</text>
      <text class="tagline" x="413" y="684">making up one unified body.</text>
    </g>

    <g class="band band-doctrine">
      <polygon role="img" aria-label="Photo: hand resting on an open Bible, tinted blue" points="0,738 710,778 710,922 0,922" fill="url(#doctrine-fill)"/>
      <text class="tagline" x="252" y="838" text-anchor="end">The expression of</text>
      <text class="tagline" x="252" y="859" text-anchor="end">a fundamental truth.</text>
      <text class="strength" x="275" y="865" textLength="365" lengthAdjust="spacingAndGlyphs">DOCTRINE</text>
    </g>

    <g class="footer">
      <rect class="social-square" x="45" y="944" width="20" height="20" rx="2"/>
      <text class="handle" x="73" y="959">/BRAVOHOPETX</text>
      <rect class="social-square" x="306" y="944" width="20" height="20" rx="2"/>
      <text class="handle" x="336" y="959">@BRAVOHOPETX</text>
      <rect class="social-square" x="557" y="944" width="20" height="20" rx="2"/>
      <text class="handle" x="588" y="959">/GraceHarbored</text>
      <text class="website" x="355" y="990" text-anchor="middle">graceharbored.org</text>
    </g>
  </svg>
</main>
</body>
</html>
```